Torven Medical needs bold attention catching website for healthcare professionals(target)

I need a hero page as well as a products and about page for a website of mine. I specialize in orthopedic instruments . Specifically bone drills and saws. This whole company was founded to bring superb quality highly discounted medical instruments. Specifically bone drills, bone saws, k-wires and pins. Two main points should be cost savings and superior quality.

Target Market(s)

healthcare professionals Surgeons and hospital material managers

Number of Pages Required

3 page

Font styles to use
Serif

Colors

Designer to choose colors to be used in the design.

Requirements
Must have
• colors should match logo design

```html
<!DOCTYPE html>
<html lang="en">
<head>
<meta charset="utf-8">
<title>Torven Medical</title>
<link rel="stylesheet" href="https://fonts.googleapis.com/css2?family=Montserrat:wght@300;400;500;700;800&display=swap">
<style>
:root{
  --navy:#1f2f5e;
  --indigo:#3d4177;
  --indigo-soft:rgba(61,65,119,.86);
  --orange:#ff9600;
  --orange-soft:rgba(255,150,0,.86);
  --cream:#fde3a3;
  --gray:#f2f2f2;
  --field:#ececec;
  --text:#5c5c5c;
  --footer:#2c2c2c;
  --white:#ffffff;
}
*{box-sizing:border-box;margin:0;padding:0}
html,body{width:1200px;height:3699px;overflow:hidden}
body{position:relative;background:var(--white);font-family:'Montserrat',sans-serif;color:var(--text)}
.abs{position:absolute}

/* nav */
.nav{position:absolute;left:0;top:0;width:1200px;height:60px;background:var(--white);z-index:5;box-shadow:0 1px 3px rgba(0,0,0,.05)}
.brand{position:absolute;display:flex;align-items:center;gap:6px;font-weight:500;color:var(--navy)}
.brand-dot{width:10px;height:10px;border-radius:50%;background:var(--orange)}
.nav .brand{left:136px;top:20px;font-size:13px}
.nav-links{position:absolute;top:19px;left:0;width:100%;font-size:16px;color:#666}
.nav-links span{position:absolute}

/* hero */
.hero{position:absolute;left:0;top:60px;width:1200px;height:629px}
.hero-title{position:absolute;left:0;width:1200px;top:248px;text-align:center;color:var(--white);font-size:34px;font-weight:600;line-height:60px;letter-spacing:.5px}
.btn-solid{position:absolute;background:var(--orange);color:var(--white);display:flex;align-items:center;justify-content:center;font-weight:500}
.hero .btn-solid{left:428px;top:422px;width:318px;height:71px;font-size:25px;border-radius:3px;letter-spacing:.5px}
.round-arrow{position:absolute;border-radius:50%;display:flex;align-items:center;justify-content:center}

/* headings */
.heading{position:absolute;font-size:32px;font-weight:400;color:var(--navy);letter-spacing:1px}
.heading b{font-weight:700}

/* products */
.product{position:absolute;top:877px;width:296px;height:207px;overflow:hidden}
.product .band{position:absolute;left:0;bottom:0;width:100%;height:58px;background:var(--indigo-soft);color:var(--white);font-size:20px;letter-spacing:1.5px;display:flex;align-items:center;justify-content:center}
.product-name{position:absolute;width:100%;top:58px;text-align:center;color:var(--white);font-size:20px;letter-spacing:1.5px}
.btn-line{position:absolute;border:2px solid rgba(255,255,255,.85);color:var(--white);display:flex;align-items:center;justify-content:center;letter-spacing:1.5px}

/* split */
.split{position:absolute;top:1204px;height:435px}
.split .over{font-size:32px;font-weight:400;color:var(--white);position:absolute;letter-spacing:1px}
.split .main{font-size:32px;font-weight:800;color:var(--white);position:absolute;letter-spacing:1px}
.split p{position:absolute;color:var(--white);font-size:13px;line-height:31px}
.split .btn-line{width:200px;height:49px;font-size:14px}

/* case studies */
.cases{position:absolute;left:0;top:1639px;width:1200px;height:620px;background:var(--gray)}
.case{position:absolute;top:1813px;width:196px;height:240px;background:var(--white)}
.case .pic{width:100%;height:189px}
.case .cap{text-align:center;color:var(--orange);font-size:13px;font-weight:500;margin-top:17px;letter-spacing:.5px}

/* blog */
.post-title{position:absolute;color:var(--white);font-size:24px;font-weight:700;letter-spacing:1px}
.post-text{position:absolute;color:var(--white);font-size:19px;line-height:33.5px;width:260px;font-weight:400}

/* stats */
.stat{position:absolute;width:126px;height:126px;border:3px solid var(--orange);border-radius:50%;display:flex;align-items:center;justify-content:center;color:var(--orange);font-size:31px;font-weight:500}
.stat-label{position:absolute;width:220px;text-align:center;font-size:16px;color:#555;letter-spacing:.5px}

/* form */
.field{position:absolute;background:var(--field);color:#8a8a8a;font-size:17px;padding-left:33px;display:flex;align-items:center;letter-spacing:.5px}
.field.area{align-items:flex-start;padding-top:20px}
.send{left:594px;top:3180px;width:259px;height:66px;font-size:19px;letter-spacing:1px}

/* footer */
.footer{position:absolute;left:0;top:3345px;width:1200px;height:354px;background:var(--footer)}
.footer .brand{left:0;width:1200px;justify-content:center;top:76px;font-size:24px;color:var(--orange)}
.social{position:absolute;top:76px;width:68px;height:68px;border-radius:50%;background:#3a3a3a}
.footer .rule{position:absolute;left:0;top:268px;width:1200px;height:1px;background:#3c3c3c}
.copy{position:absolute;top:296px;width:1200px;text-align:center;color:#e8e8e8;font-size:20px;letter-spacing:1px}
</style>
</head>
<body>

<header class="nav">
  <div class="brand"><span class="brand-dot"></span>Torven Medical</div>
  <nav class="nav-links">
    <span style="left:487px">Home</span>
    <span style="left:583px">Products</span>
    <span style="left:705px">About</span>
    <span style="left:802px">Case Studies</span>
    <span style="left:959px">Blog</span>
    <span style="left:1042px">Contact</span>
  </nav>
</header>

<section class="hero">
  <svg class="abs" style="left:0;top:0" width="1200" height="629" viewBox="0 0 1200 629">
    <defs>
      <linearGradient id="heroPhoto" x1="0" y1="0" x2="1" y2="0">
        <stop offset="0" stop-color="#7e8496"/>
        <stop offset=".45" stop-color="#8b90a4"/>
        <stop offset=".75" stop-color="#5d6ea8"/>
        <stop offset="1" stop-color="#6c7db3"/>
      </linearGradient>
    </defs>
    <g role="img" aria-label="Physiotherapist helping a patient walk with crutches and a knee brace">
      <polygon points="0,0 1200,0 1200,612 0,528" fill="url(#heroPhoto)"/>
      <polygon points="0,0 1200,0 1200,612 0,528" fill="rgba(60,64,110,.35)"/>
    </g>
    <polygon points="0,528 1200,612 1200,629 0,544" fill="var(--cream)"/>
    <polygon points="0,544 1200,629 0,629" fill="var(--white)"/>
  </svg>
  <div class="round-arrow" style="left:43px;top:256px;width:72px;height:72px;background:rgba(224,170,60,.85)">
    <svg width="24" height="24" viewBox="0 0 24 24"><path d="M15 4 L7 12 L15 20" fill="none" stroke="#fff" stroke-width="3"/></svg>
  </div>
  <div class="round-arrow" style="left:1081px;top:256px;width:72px;height:72px;background:rgba(224,170,60,.85)">
    <svg width="24" height="24" viewBox="0 0 24 24"><path d="M9 4 L17 12 L9 20" fill="none" stroke="#fff" stroke-width="3"/></svg>
  </div>
  <h1 class="hero-title">We bring superb quality highly discounted<br>medical instruments to you</h1>
  <div class="btn-solid">Get Started</div>
</section>

<h2 class="heading" style="left:123px;top:756px">OUR <b>PRODUCTS</b></h2>

<div class="product" style="left:131px">
  <div role="img" aria-label="Surgeons operating under a surgical lamp" style="width:100%;height:100%;background:linear-gradient(135deg,#2f6fa0,#7fb0d2 50%,#2a5a86)"></div>
  <div class="band">BONE DRILLS</div>
</div>
<div class="product" style="left:451px;background:var(--indigo)">
  <div role="img" aria-label="Bone saw in use" style="position:absolute;inset:0;background:linear-gradient(135deg,#4a4f85,#5b5f94)"></div>
  <div class="product-name">BONE SAWS</div>
  <div class="btn-line" style="left:53px;top:100px;width:186px;height:45px;font-size:16px">VIEW</div>
</div>
<div class="product" style="left:769px">
  <div role="img" aria-label="Doctor examining a patient's knee" style="width:100%;height:100%;background:linear-gradient(135deg,#e8e4e0,#d9c2ad 55%,#c9d0dc)"></div>
  <div class="band">K-WIRES</div>
</div>
<div class="round-arrow" style="left:143px;top:936px;width:52px;height:52px;background:var(--orange)">
  <svg width="22" height="22" viewBox="0 0 22 22"><path d="M19 11 H4 M10 4 L3 11 L10 18" fill="none" stroke="#fff" stroke-width="3"/></svg>
</div>
<div class="round-arrow" style="left:997px;top:936px;width:52px;height:52px;background:var(--orange)">
  <svg width="22" height="22" viewBox="0 0 22 22"><path d="M3 11 H18 M12 4 L19 11 L12 18" fill="none" stroke="#fff" stroke-width="3"/></svg>
</div>

<section class="split" style="left:0;width:594px">
  <div role="img" aria-label="Team of smiling medical staff" style="position:absolute;inset:0;background:linear-gradient(135deg,#6d6f96,#4a4d80 60%,#3c3f74)"></div>
  <div style="position:absolute;inset:0;background:rgba(61,65,119,.55)"></div>
  <div class="over" style="left:90px;top:114px">MEET</div>
  <div class="main" style="left:90px;top:166px">OUR TEAM</div>
  <p style="left:96px;top:213px">Lorem ipsum dolor sit amet, consectetur adipiscing elit.<br>Fusce commodo metus vitae neque tempor dapibus.</p>
  <div class="btn-line" style="left:96px;top:290px">VIEW MORE</div>
</section>
<section class="split" style="left:594px;width:606px">
  <div role="img" aria-label="Hospital operating room with equipment" style="position:absolute;inset:0;background:linear-gradient(135deg,#f4a22a,#f7ad3f 50%,#f19a18)"></div>
  <div style="position:absolute;inset:0;background:rgba(255,150,0,.55)"></div>
  <div class="over" style="left:92px;top:114px">LEARN</div>
  <div class="main" style="left:92px;top:166px">ABOUT US</div>
  <p style="left:92px;top:213px">Lorem ipsum dolor sit amet, consectetur adipiscing elit.<br>Fusce commodo metus vitae neque tempor dapibus.</p>
  <div class="btn-line" style="left:94px;top:290px">VIEW MORE</div>
</section>

<section class="cases"></section>
<h2 class="heading" style="left:125px;top:1715px">OUR <b>CASE STUDIES</b></h2>
<svg class="abs" style="left:1070px;top:1723px" width="40" height="20" viewBox="0 0 40 20">
  <path d="M12 4 L6 10 L12 16" fill="none" stroke="var(--orange)" stroke-width="2.5"/>
  <path d="M28 4 L34 10 L28 16" fill="none" stroke="#222" stroke-width="2.5"/>
</svg>
<div class="case" style="left:257px"><div class="pic" role="img" aria-label="Surgical loupes held above an open hand" style="background:linear-gradient(135deg,#c9d3dc,#9aa7b3)"></div><div class="cap">Lorem ipsum dolor</div></div>
<div class="case" style="left:477px"><div class="pic" role="img" aria-label="Bandaged arm being treated" style="background:linear-gradient(135deg,#d9c7b8,#efe9e3 50%,#b9a596)"></div><div class="cap">Lorem ipsum dolor</div></div>
<div class="case" style="left:697px"><div class="pic" role="img" aria-label="Surgeon in mask during an operation" style="background:linear-gradient(135deg,#5f7f97,#9bb3c4 50%,#42607a)"></div><div class="cap">Lorem ipsum dolor</div></div>
<div class="case" style="left:917px;box-shadow:0 4px 10px rgba(0,0,0,.12)">
  <div class="pic" role="img" aria-label="Lab researcher at a microscope" style="background:linear-gradient(135deg,#f5b43a,#f8c45a 50%,#f0a623);position:relative">
    <svg class="abs" style="left:72px;top:82px" width="48" height="26" viewBox="0 0 48 26"><path d="M2 13 H44 M33 2 L45 13 L33 24" fill="none" stroke="#fff" stroke-width="2.5"/></svg>
  </div>
  <div class="cap">Lorem ipsum dolor</div>
</div>
<div class="case" style="left:1138px"><div class="pic" role="img" aria-label="Doctor in a white coat" style="background:linear-gradient(135deg,#6a6e78,#d5d8dc)"></div><div class="cap">Lorem</div></div>

<svg class="abs" style="left:0;top:2128px" width="1200" height="550" viewBox="0 0 1200 550">
  <defs>
    <linearGradient id="blogPhoto" x1="0" y1="0" x2="1" y2="0">
      <stop offset="0" stop-color="#3e4277"/>
      <stop offset=".55" stop-color="#444a80"/>
      <stop offset="1" stop-color="#3a3e72"/>
    </linearGradient>
  </defs>
  <polygon points="0,98 1200,0 1200,14 0,112" fill="var(--white)"/>
  <polygon points="0,112 1200,14 1200,550 0,550" fill="url(#blogPhoto)" role="img" aria-label="Microscope in a laboratory, dimmed behind a blue tint"/>
</svg>
<h2 class="heading" style="left:141px;top:2289px;color:var(--white)">OUR <b>BLOG</b></h2>
<div class="abs" style="left:141px;top:2355px;width:904px;height:1px;background:rgba(255,255,255,.18)"></div>

<div class="abs" role="img" aria-label="Doctor with glasses talking to a patient" style="left:141px;top:2406px;width:178px;height:222px;background:linear-gradient(135deg,#dfe3e6,#b8c4cc 50%,#7f8f9c)"></div>
<h3 class="post-title" style="left:334px;top:2416px">LOREM IPSUM</h3>
<p class="post-text" style="left:335px;top:2457px">Lorem ipsum dolor sit amet, consectetur adip-iscing elit. Fusce commo-do metus vitae neque tempor dapibus. Donec</p>

<div class="abs" role="img" aria-label="Medical staff walking down a hospital corridor" style="left:627px;top:2406px;width:178px;height:222px;background:linear-gradient(135deg,#e6eef2,#a9c6d4 50%,#4f8fae)"></div>
<h3 class="post-title" style="left:819px;top:2416px">LOREM IPSUM</h3>
<p class="post-text" style="left:820px;top:2457px">Lorem ipsum dolor sit amet, consectetur adip-iscing elit. Fusce commo-do metus vitae neque tempor dapibus. Donec</p>

<h2 class="heading" style="left:593px;top:2773px">GET <b>IN TOUCH</b></h2>

<div class="stat" style="left:125px;top:2861px">169</div>
<div class="stat" style="left:319px;top:2861px">15K</div>
<div class="stat" style="left:125px;top:3068px">542</div>
<div class="stat" style="left:319px;top:3068px">296</div>
<div class="stat-label" style="left:80px;top:3009px">Licensced products</div>
<div class="stat-label" style="left:278px;top:3009px">Satisfied Clients</div>
<div class="stat-label" style="left:87px;top:3217px">Case Completed</div>
<div class="stat-label" style="left:271px;top:3217px">Awards won</div>

<div class="field" style="left:591px;top:2855px;width:493px;height:59px">Your Name</div>
<div class="field" style="left:591px;top:2944px;width:237px;height:59px">Your Email</div>
<div class="field" style="left:847px;top:2944px;width:237px;height:59px">Your Phone</div>
<div class="field area" style="left:591px;top:3030px;width:493px;height:108px">Your Message</div>
<div class="btn-solid send">SEND MESSAGE</div>

<footer class="footer">
  <div class="brand"><span class="brand-dot"></span>Torven Medical</div>
  <div class="social" style="left:394px;top:165px" role="img" aria-label="Social profile"></div>
  <div class="social" style="left:478px;top:165px" role="img" aria-label="Social profile"></div>
  <div class="social" style="left:566px;top:165px" role="img" aria-label="Social profile"></div>
  <div class="social" style="left:649px;top:165px" role="img" aria-label="Social profile"></div>
  <div class="social" style="left:728px;top:165px" role="img" aria-label="Social profile"></div>
  <div class="rule"></div>
  <div class="copy">© 2019 Torven Medical copyright</div>
</footer>

</body>
</html>
```